Locksmith Business Cards

My father-in-law is in need of new business cards for his locksmith business and I need to impress him. Kindly help me out!

You can see the previous business card attached. It is a family run business in North Wales.

No individual names on the cards.

Key Things to Feature:
- The words "Prompt", "Local", "Reliable" (as you can see under the logo on the website)
- 24h Emergency Service
- Covering All of North Wales, the Wirral and Chester
- The color blue
- A key or a lock would be interesting (similar to the ones that come up when you google locksmith business card)

Optional (only if design includes bullet points, like the example below):
https://imgvaultcdnx.net/design_img/318264/57190/57190_2749031_318264_image.jpg
- Residential / Commercial / Automotive
- Alarms & Cameras
- Key Cutting & Safes

https://www.bryncoed-locksmiths-demo.co.uk/

Locksmith

01632 960 418
07700 900 362
bryncoedlocksmiths@mailvalex.com
Bryncoed Locksmiths, Hafod Barn, 4 Pennant Rd., Penrhyndre LL39 7QZ
www.bryncoed-locksmiths-demo.co.uk

• - The words "Prompt", "Local", "Reliable" (as you can see under the logo on the website)
• - 24h Emergency Service
• - Covering All of North Wales, the Wirral and Chester
• - A key or a lock would be interesting (similar to the ones that come up when you google locksmith business card)

```html
<!DOCTYPE html>
<html lang="en">
<head>
<meta charset="utf-8">
<title>Bryncoed Locksmith – Business Cards</title>
<link rel="stylesheet" href="https://fonts.googleapis.com/css2?family=Lato:wght@400;700;900&family=Raleway:wght@300;400&display=swap">
<style>
  :root {
    --stage: #1c1c1e;
    --navy: #0a1670;
    --electric: #0a20f0;
    --royal: #3450b4;
    --white: #ffffff;
    --dot-core: #fff4e0;
    --dot-ring: #f2a23a;
    --photo-sky: #b9cde0;
    --photo-hill: #5c7560;
    --photo-road: #8c8e92;
  }
  * { box-sizing: border-box; margin: 0; padding: 0; }
  html, body { width: 1200px; height: 894px; overflow: hidden; }
  body {
    background: var(--stage);
    font-family: "Lato", Arial, sans-serif;
    color: var(--white);
    position: relative;
  }
  .card {
    position: absolute;
    left: 250px;
    width: 700px;
    height: 400px;
    overflow: hidden;
  }
  .card--front { top: 30px; background: var(--electric); }
  .card--back { top: 464px; background: var(--royal); }
  .card__shapes { position: absolute; inset: 0; width: 700px; height: 400px; }

  .brand { position: absolute; text-align: center; line-height: 1; white-space: nowrap; }
  .brand__name { font-weight: 900; font-size: 22px; letter-spacing: 1px; text-transform: uppercase; }
  .brand__since { font-family: "Raleway", sans-serif; font-size: 13px; font-variant: small-caps; margin-top: 5px; letter-spacing: 0.5px; }
  .card--front .brand { left: 40px; top: 32px; width: 320px; }

  .values { position: absolute; left: 36px; top: 128px; display: flex; gap: 16px; font-size: 21px; letter-spacing: 0.5px; }
  .values__item { display: flex; align-items: center; gap: 6px; }
  .values__dot {
    width: 15px; height: 15px; border-radius: 50%;
    background: radial-gradient(circle at 40% 40%, var(--dot-core) 45%, var(--dot-ring) 100%);
  }

  .pill {
    position: absolute;
    border: 1.5px solid var(--white);
    border-radius: 24px;
    text-align: center;
  }
  .pill--emergency { left: 76px; top: 188px; padding: 7px 20px; font-size: 21px; letter-spacing: 0.5px; white-space: nowrap; }

  .services { position: absolute; left: 76px; top: 266px; list-style: none; font-size: 15px; line-height: 1.3; letter-spacing: 0.3px; }

  .card--back .pill--brand { left: 395px; top: 62px; width: 285px; padding: 16px 10px; border-radius: 16px; }
  .card--back .pill--brand .brand { position: static; }

  .contacts { position: absolute; left: 392px; top: 196px; list-style: none; font-family: "Raleway", sans-serif; font-weight: 300; font-size: 14px; line-height: 1.35; white-space: nowrap; }
  .contacts__row { display: flex; align-items: center; gap: 12px; margin-bottom: 10px; }
  .contacts__icon { width: 20px; height: 20px; flex: none; }
</style>
</head>
<body>

<section class="card card--front" aria-label="Business card front">
  <svg class="card__shapes" viewBox="0 0 700 400" aria-hidden="true">
    <defs>
      <linearGradient id="photoToneA" x1="0" y1="0" x2="0" y2="1">
        <stop offset="0" stop-color="var(--photo-sky)"/>
        <stop offset="0.5" stop-color="var(--photo-hill)"/>
        <stop offset="1" stop-color="var(--photo-road)"/>
      </linearGradient>
    </defs>
    <polygon points="0,0 445,0 452,105 0,105" fill="var(--navy)"/>
    <polygon points="445,0 453,0 462,60 454,60" fill="var(--white)"/>
  </svg>
  <svg class="card__shapes" viewBox="0 0 700 400" role="img" aria-label="Photo of a grey SUV driving on a road beneath green mountains">
    <polygon points="455,0 700,0 700,400 650,400" fill="url(#photoToneA)"/>
  </svg>

  <div class="brand">
    <div class="brand__name">Bryncoed Locksmith</div>
    <div class="brand__since">Since 1989</div>
  </div>

  <div class="values">
    <span class="values__item"><i class="values__dot"></i>PROMPT</span>
    <span class="values__item"><i class="values__dot"></i>LOCAL</span>
    <span class="values__item"><i class="values__dot"></i>RELIABLE</span>
  </div>

  <div class="pill pill--emergency">24H EMERGANCY SERVICE</div>

  <ul class="services">
    <li>Residential / Commercial / Automotive</li>
    <li>Alarms &amp; Cameras</li>
    <li>Key Cutting &amp; Safes</li>
  </ul>
</section>

<section class="card card--back" aria-label="Business card back">
  <svg class="card__shapes" viewBox="0 0 700 400" aria-hidden="true">
    <polygon points="250,0 330,0 300,50" fill="var(--white)"/>
    <polygon points="330,330 390,380 330,400 300,400" fill="var(--white)"/>
  </svg>
  <svg class="card__shapes" viewBox="0 0 700 400" role="img" aria-label="Photo of a grey SUV driving on a road beneath green mountains">
    <defs>
      <linearGradient id="photoToneB" x1="0" y1="0" x2="0" y2="1">
        <stop offset="0" stop-color="var(--photo-sky)"/>
        <stop offset="0.5" stop-color="var(--photo-hill)"/>
        <stop offset="1" stop-color="var(--photo-road)"/>
      </linearGradient>
    </defs>
    <polygon points="0,0 250,0 340,160 335,330 300,400 0,400" fill="url(#photoToneB)"/>
  </svg>

  <div class="pill pill--brand">
    <div class="brand">
      <div class="brand__name">Bryncoed Locksmith</div>
      <div class="brand__since">Since 1989</div>
    </div>
  </div>

  <ul class="contacts">
    <li class="contacts__row">
      <svg class="contacts__icon" viewBox="0 0 20 20" aria-hidden="true"><circle cx="10" cy="10" r="9" fill="none" stroke="#fff" stroke-width="1.4"/><path d="M7 5.5l1.6 2.2-1 1.2a6 6 0 0 0 3.5 3.5l1.2-1 2.2 1.6-.9 1.6c-3.6-.2-7-3.6-7.2-7.2z" fill="#fff"/></svg>
      <span>01632 960 418<br>07700 900 362</span>
    </li>
    <li class="contacts__row">
      <svg class="contacts__icon" viewBox="0 0 20 20" aria-hidden="true"><circle cx="10" cy="10" r="9" fill="none" stroke="#fff" stroke-width="1.4"/><rect x="5.5" y="7" width="9" height="6.5" fill="none" stroke="#fff" stroke-width="1.2"/><path d="M5.5 7l4.5 3.5L14.5 7" fill="none" stroke="#fff" stroke-width="1.2"/></svg>
      <span>bryncoedlocksmiths@mailvalex.com</span>
    </li>
    <li class="contacts__row">
      <svg class="contacts__icon" viewBox="0 0 20 20" aria-hidden="true"><circle cx="10" cy="10" r="9" fill="none" stroke="#fff" stroke-width="1.4"/><path d="M10 15.5s-4-4-4-6.7a4 4 0 0 1 8 0c0 2.7-4 6.7-4 6.7z" fill="#fff"/><circle cx="10" cy="8.8" r="1.5" fill="var(--royal)"/></svg>
      <span>Bryncoed Locksmiths, Hafod Barn,<br>4 Pennant Rd., Penrhyndre LL39 7QZ</span>
    </li>
    <li class="contacts__row">
      <svg class="contacts__icon" viewBox="0 0 20 20" aria-hidden="true"><circle cx="10" cy="10" r="9" fill="none" stroke="#fff" stroke-width="1.4"/><circle cx="10" cy="10" r="5" fill="none" stroke="#fff" stroke-width="1"/><path d="M5 10h10M10 5c-2 3-2 7 0 10M10 5c2 3 2 7 0 10" fill="none" stroke="#fff" stroke-width="1"/></svg>
      <span>www.bryncoed-locksmiths-demo.co.uk</span>
    </li>
  </ul>
</section>

</body>
</html>
```